A church planting organization designed specifically for the urban centers

I am looking to create a 5 page website.

i would like to create an (1) Homepage, (2) About Us, (3) Donate, (4) Contact Us, and (5) Partner Page

The name of the organization is called Harborline Faith Builders which is an organization designed to help establish churches in a central city context.

I would like the colors to incorporate the colors of the logo which is a black, white, and orange. I would be okay with adding a
green for an accent. I love the use of orange filters when appropriate.

We would like to have a design that pops at first glance. I have included some graphs that can be recreated or recolored to better fit with one's design.

Primary Goal:
A marketing tool to attract (1) Harborline Faith Builders who desire to plant and; (2) donors; (3) churches or church plant networks that have an interest in partnering financially or through collective impact. Information should be provided on how to become part of the movement.

Secondary Goal:
Make the argument why central city church plants are needed
Make the argument why Multi-Ethnic churches are needed
Candidates can apply for residency at one of the network churches
Churches can apply to join the network
Church Planting Networks can apply to partner

Target Market(s)

Target Market
Church Planting Networks
Ethnic Homogenous Churches
Church Networks
Church Planters
Diversity Seekers
Impactors of Distressed Communities

Coding

Coded - Design and coding required

Number of Pages Required

5+ page

Font styles to use
Other font styles liked:
• I have uploaded our font

Requirements
Must have
• Pages that pop at first glance
Nice to have
• I would like the graphs I attached recreated or recolored to match your design layout

```html
<!DOCTYPE html>
<html lang="en">
<head>
<meta charset="utf-8">
<title>Harborline Faith Builders</title>
<link rel="stylesheet" href="https://fonts.googleapis.com/css2?family=Montserrat:wght@300;400;500;600;700&display=swap">
<style>
:root{
  --orange:#f26b1d;
  --orange-dark:#d9560f;
  --ink:#1f1f1f;
  --text:#444;
  --muted:#777;
  --teal-deep:#0b3034;
  --brown-deep:#4b2a0e;
  --purple-deep:#241a4e;
  --purple-mid:#3a2a7a;
  --footer:#2a2a2a;
  --partner-band:#1c1c1c;
  --line:#555;
  --white:#fff;
}
*{margin:0;padding:0;box-sizing:border-box}
html,body{width:1200px;height:3940px;overflow:hidden}
body{position:relative;font-family:'Montserrat',sans-serif;color:var(--text);background:var(--white)}
.abs{position:absolute}

/* header */
.brand{position:absolute;left:120px;top:30px;display:flex;align-items:center;gap:10px}
.brand-dot{width:26px;height:26px;border-radius:50%;background:var(--orange)}
.brand-name{font-weight:700;font-size:15px;color:var(--ink);line-height:1.15;width:130px}
.nav{position:absolute;top:52px;left:503px;display:flex;align-items:center;font-size:13px;color:var(--ink)}
.nav a{color:inherit;text-decoration:none;position:absolute;white-space:nowrap}
.btn-donate{display:inline-block;background:linear-gradient(#ffb15e,var(--orange));border:1px solid var(--orange-dark);border-radius:14px;color:#3a1d07;font-weight:700;font-style:normal;font-size:12px;text-align:center;line-height:21px;height:23px}

/* hero */
.hero-bg{position:absolute;left:0;top:0;width:1200px;height:700px;background:linear-gradient(180deg,#e6e6e8 0%,#f3f3f4 55%,#fff 100%)}
.hero-houses{position:absolute;left:520px;top:0;width:680px;height:660px;background:radial-gradient(ellipse at 60% 35%,#c9c9cd 0%,#e4e4e6 55%,rgba(255,255,255,0) 80%)}
.hero-mark{position:absolute;left:520px;top:160px;width:650px;height:490px;display:flex;flex-direction:column;align-items:center;justify-content:center;gap:18px}
.hero-mark .ring{width:150px;height:150px;border-radius:50%;background:radial-gradient(circle at 40% 40%,#8b3fd6,#3a1670)}
.hero-mark .word{font-size:46px;font-weight:700;color:#2a1150;letter-spacing:2px;text-align:center}
.hero-eyebrow{position:absolute;left:118px;top:262px;font-size:32px;font-weight:400;color:var(--ink);letter-spacing:.5px}
.hero-title{position:absolute;left:112px;top:298px;font-size:52px;font-weight:700;color:var(--ink);line-height:62px}
.hl{background:var(--orange);color:#fff;border-radius:30px 0 0 30px;padding:0 6px 0 10px;box-shadow:0 6px 14px rgba(242,107,29,.35)}
.hero-lede{position:absolute;left:112px;top:422px;width:345px;font-size:12.5px;line-height:20px;color:var(--ink)}
.hero-donate{position:absolute;left:112px;top:502px;width:116px}
.call{position:absolute;left:112px;top:622px;display:flex;gap:8px;align-items:center}
.call-icon{width:22px;height:36px;border-radius:5px;background:#3aa655;display:flex;align-items:center;justify-content:center}
.call small{display:block;font-size:12px;color:#555}
.call strong{display:block;font-size:20px;font-weight:600;color:var(--ink)}

/* section titles */
.sec-title{position:absolute;font-size:40px;font-weight:700;color:var(--ink);white-space:nowrap}
.sec-title.center{left:0;width:1200px;text-align:center}
.sec-title.light{color:#fff}

/* problem */
.problem-photo{position:absolute;left:112px;top:782px;width:391px;height:335px;background:linear-gradient(135deg,#2c2a16 0%,#6d7a2a 40%,#c8e07a 55%,#3a2a18 100%)}
.problem-title{left:532px;top:797px}
.problem-copy{position:absolute;left:532px;top:860px;width:560px;font-size:14.5px;line-height:24.6px;font-weight:300;color:var(--text)}
.btn-dark{position:absolute;background:#1f1f1f;color:#fff;font-size:12.5px;font-weight:600;border-radius:22px;text-align:center;letter-spacing:.3px}

/* barrier */
.barrier{position:absolute;left:0;top:1216px;width:1200px;height:740px;background:linear-gradient(180deg,var(--teal-deep) 0%,#1e2f1e 45%,var(--brown-deep) 100%)}
.barrier-tree{position:absolute;left:400px;top:1380px;width:400px;height:560px;background:radial-gradient(ellipse at 50% 45%,rgba(90,170,80,.45) 0%,rgba(200,100,30,.35) 45%,rgba(0,0,0,0) 72%)}
.barrier-label{position:absolute;color:#fff;font-size:15px;line-height:21px;font-weight:300}
.barrier-label b{font-weight:500}
.barrier-label.right{text-align:right}
.leader{position:absolute;border-color:rgba(255,255,255,.6);border-style:dotted;border-width:0}
.tick{display:inline-block;width:5px;height:5px;border-radius:50%;background:var(--orange);vertical-align:middle;margin:0 4px}

/* faq */
.faq-pill{position:absolute;height:38px;width:392px;background:#2b2b2b;border-radius:19px;color:#fff;font-size:14px;font-weight:600;display:flex;align-items:center;padding:0 18px}
.faq-pill .q{width:12px;height:12px;border:2px solid var(--orange);border-radius:50%;margin-right:18px}
.faq-pill .plus{margin-left:auto;font-weight:400;font-size:16px}

/* about */
.about-bg{position:absolute;left:0;top:2380px;width:1200px;height:605px;background:radial-gradient(ellipse at 75% 20%,#4a3a8a 0%,var(--purple-mid) 35%,var(--purple-deep) 80%)}
.card{position:absolute;top:2565px;width:224px}
.card-photo{height:203px}
.card h3{margin-top:22px;font-size:16px;font-weight:600;color:#fff}
.card p{margin-top:8px;font-size:13.5px;line-height:21px;color:rgba(255,255,255,.55);font-weight:300}
.btn-orange{display:block;margin-top:14px;margin-left:2px;width:124px;height:39px;line-height:39px;border-radius:20px;background:var(--orange);color:#fff;font-size:12.5px;font-weight:600;text-align:center}
.slide-arrow{position:absolute;top:2647px;width:40px;height:40px;border-radius:50%;border:1px solid rgba(255,255,255,.35);color:#fff;font-size:14px;text-align:center;line-height:38px}

/* contact */
.field{position:absolute;border-bottom:1px solid var(--line);font-size:12.5px;color:var(--ink);padding-bottom:14px}

/* partner band */
.partner-strip{position:absolute;left:0;top:3510px;width:1200px;height:78px;background:#f2f2f2}
.partner-tab{position:absolute;left:0;top:3510px;width:420px;height:78px;background:var(--partner-band);clip-path:polygon(0 0,340px 0,420px 78px,0 78px)}
.partner-tab span{position:absolute;left:112px;top:18px;font-size:36px;font-weight:700;color:#fff}
.badge{position:absolute;top:3535px;height:28px;width:120px;border-radius:4px;background:#8a8a8a;opacity:.6}

/* footer */
.footer{position:absolute;left:0;top:3588px;width:1200px;height:352px;background:var(--footer);color:#c9c9c9}
.footer h4{position:absolute;top:68px;font-size:15px;font-weight:600;color:#fff;letter-spacing:.4px}
.footer ul{position:absolute;list-style:none;font-size:12.5px;line-height:28px}
.footer .mission{position:absolute;left:112px;top:104px;width:310px;font-size:13px;line-height:23px}
.f-brand{position:absolute;left:118px;top:190px;display:flex;align-items:center;gap:10px}
.f-brand .brand-name{color:#fff}
.contact-row{position:absolute;left:710px;display:flex;gap:8px;font-size:12px;line-height:17px}
.pin{width:9px;height:12px;flex:none;margin-top:2px}
.social{position:absolute;left:992px;display:flex;align-items:center;gap:8px;font-size:12.5px}
.social i{width:26px;height:26px;border-radius:50%;background:#fff;display:inline-block}
.copy{position:absolute;left:0;width:1200px;top:280px;text-align:center;font-size:11px;color:#9a9a9a}
.copy b{color:#fff;font-weight:500}
</style>
</head>
<body>

<!-- hero -->
<div class="hero-bg"></div>
<div class="hero-houses" role="img" aria-label="Faded photograph of city row houses"></div>

<header>
  <div class="brand"><span class="brand-dot"></span><span class="brand-name">Harborline Faith Builders</span></div>
  <nav class="nav">
    <a style="left:0">Home</a>
    <a style="left:85px">About Us</a>
    <a style="left:189px">Donate</a>
    <a style="left:283px">Partner</a>
    <a style="left:377px">Contact Us</a>
  </nav>
  <span class="btn-donate abs" style="left:970px;top:50px;width:115px">Donate</span>
</header>

<div class="hero-mark" role="img" aria-label="Large emblem with the organization name above silhouettes of people and roots">
  <span class="ring"></span>
  <span class="word">Harborline Faith Builders</span>
</div>

<div class="hero-eyebrow">HARBORLINE</div>
<h1 class="hero-title"><span class="hl">FAITH</span> BUILDERS</h1>
<p class="hero-lede">To multiply the gospel in urban centers by raising up and equipping church planters in a central city or multi-ethnic context.</p>
<span class="btn-donate hero-donate">Donate</span>
<div class="call">
  <span class="call-icon"><svg width="12" height="14" viewBox="0 0 12 14"><path d="M3 1l2 3-1.5 1.5c.6 1.6 1.8 2.9 3.4 3.6L8.5 7.5l3 2-1 2.5C6 12 1.5 7.5 1 2z" fill="#fff"/></svg></span>
  <div><small>Call Us Today:</small><strong>+1 (555) 014 2290</strong></div>
</div>

<!-- problem -->
<div class="problem-photo" role="img" aria-label="Photograph of a pastor speaking on a stage in front of a worship screen"></div>
<h2 class="sec-title problem-title"><span class="hl">PRO</span>BLEM</h2>
<p class="problem-copy">The church planting scene in the central city of Riverton is fairly problematic. While church planting networks have been planting many churches in a suburban context each year, the central city has been ignored. Unfortunately, many church planting organizations have little to no understanding of the central city context and have therefore avoided planting central city churches in Riverton and beyond.To exacerbate the issue, Black churches historically do not plant churches.</p>
<span class="btn-dark" style="left:532px;top:1050px;width:136px;height:40px;line-height:40px">READ MORE</span>

<!-- barrier -->
<section>
  <div class="barrier"></div>
  <h2 class="sec-title center light" style="top:1270px"><span class="hl">BAR</span>RIER TO ADDRESS</h2>
  <div class="barrier-tree" role="img" aria-label="Illustration of a growing tree with five hexagon icons on its branches and roots below"></div>

  <div class="leader" style="left:765px;top:1392px;width:70px;height:38px;border-top-width:1px;border-right-width:1px"></div>
  <div class="barrier-label" style="left:852px;top:1416px"><span class="tick" style="margin-left:-9px"></span><b>Suburban<br>Support Raising Model</b></div>

  <div class="leader" style="left:345px;top:1468px;width:84px;height:45px;border-top-width:1px;border-left-width:1px"></div>
  <div class="barrier-label right" style="left:140px;top:1503px;width:208px">Launch Team<span class="tick"></span></div>

  <div class="leader" style="left:795px;top:1570px;width:45px;height:24px;border-bottom-width:1px;border-right-width:1px"></div>
  <div class="barrier-label" style="left:852px;top:1560px"><span class="tick" style="margin-left:-9px"></span>Church<br>Planter Assessment</div>

  <div class="leader" style="left:366px;top:1655px;width:64px;height:50px;border-bottom-width:1px;border-left-width:1px"></div>
  <div class="barrier-label right" style="left:120px;top:1645px;width:232px">Cultural Competency<span class="tick"></span></div>

  <div class="leader" style="left:782px;top:1708px;width:58px;height:52px;border-bottom-width:1px;border-right-width:1px"></div>
  <div class="barrier-label" style="left:852px;top:1696px"><span class="tick" style="margin-left:-9px"></span>Cultural<br>Communication Priority</div>

  <svg class="abs" style="left:0;top:1820px" width="1200" height="140" viewBox="0 0 1200 140" aria-hidden="true">
    <path d="M0 68 C120 40 250 60 380 70 C520 82 620 100 760 108 C900 116 1050 80 1200 40 L1200 140 L0 140Z" fill="#fff"/>
    <path d="M780 118 C820 116 850 112 880 104" stroke="#7fd6d0" stroke-width="2" fill="none"/>
  </svg>
</section>

<!-- faq -->
<section>
  <h2 class="sec-title center" style="top:2028px"><span class="hl">F</span>AQ</h2>
  <div class="faq-pill" style="left:195px;top:2115px"><span class="q"></span>Why partner with HFB?<span class="plus">+</span></div>
  <div class="faq-pill" style="left:613px;top:2115px"><span class="q"></span>Who Do We Partner With?<span class="plus">+</span></div>
  <div class="faq-pill" style="left:195px;top:2170px"><span class="q"></span>How do my network partner with HFB?<span class="plus">+</span></div>
  <div class="faq-pill" style="left:613px;top:2170px"><span class="q"></span>I want to plant a church, what do I do?<span class="plus">+</span></div>
  <span class="btn-dark" style="left:519px;top:2237px;width:162px;height:41px;line-height:41px">VIEW MORE FAQ</span>
</section>

<!-- about -->
<section>
  <div class="about-bg" role="img" aria-label="Purple tinted photograph of a worship gathering"></div>
  <svg class="abs" style="left:0;top:2360px" width="1200" height="80" viewBox="0 0 1200 80" aria-hidden="true">
    <path d="M0 0 H1200 V40 C1100 66 1000 70 900 54 C780 34 700 10 560 24 C420 38 300 60 180 56 C100 52 40 40 0 34Z" fill="#fff"/>
    <path d="M500 46 C540 32 570 26 600 24" stroke="#7fd6d0" stroke-width="2" fill="none"/>
  </svg>
  <h2 class="sec-title center light" style="top:2488px"><span class="hl">AB</span>OUT US</h2>
  <span class="slide-arrow" style="left:35px">&lsaquo;</span>
  <span class="slide-arrow" style="left:1125px">&rsaquo;</span>

  <div class="card" style="left:112px">
    <div class="card-photo" role="img" aria-label="Portrait photograph of a team member" style="background:linear-gradient(160deg,#7a6450,#d8c6b4)"></div>
    <h3>Dana Whitfield</h3>
    <p>Dana Whitfield along with her husband...</p>
    <span class="btn-orange">READ MORE</span>
  </div>
  <div class="card" style="left:362px">
    <div class="card-photo" role="img" aria-label="Portrait photograph of a team member" style="background:linear-gradient(160deg,#3a2c22,#8a6a50)"></div>
    <h3>Paul Arden</h3>
    <p>Paul Arden is a church planter and has been the Lead ...</p>
    <span class="btn-orange">READ MORE</span>
  </div>
  <div class="card" style="left:612px">
    <div class="card-photo" role="img" aria-label="Portrait photograph of a team member" style="background:linear-gradient(160deg,#9a8a78,#3a3434)"></div>
    <h3>Marcus Hale</h3>
    <p>Marcus Hale II is a Native Born of Riverton...</p>
    <span class="btn-orange">READ MORE</span>
  </div>
  <div class="card" style="left:862px">
    <div class="card-photo" role="img" aria-label="Portrait photograph of a team member" style="background:linear-gradient(160deg,#5a3a2a,#e06a2a)"></div>
    <h3>Andre Booker</h3>
    <p>Andre Booker was born and raised as a preacher's...</p>
    <span class="btn-orange">READ MORE</span>
  </div>
</section>

<!-- quick contact -->
<section>
  <h2 class="sec-title center" style="top:3068px"><span class="hl">QUICK</span> CONTACT</h2>
  <div class="field" style="left:270px;top:3160px;width:316px">Name:</div>
  <div class="field" style="left:613px;top:3160px;width:317px">Email:</div>
  <div class="field" style="left:270px;top:3215px;width:316px">Phone:</div>
  <div class="field" style="left:613px;top:3215px;width:317px">Organization:</div>
  <div class="field" style="left:270px;top:3273px;width:660px;height:100px">Comments:</div>
  <span class="btn-dark" style="left:272px;top:3387px;width:124px;height:40px;line-height:40px;font-size:11.5px">SUBMIT HERE</span>
</section>

<!-- partner -->
<section>
  <div class="partner-strip"></div>
  <div class="partner-tab"><span>PARTNER</span></div>
  <span class="badge" style="left:445px"></span>
  <span class="badge" style="left:650px;width:90px"></span>
  <span class="badge" style="left:835px;width:86px"></span>
  <span class="badge" style="left:1005px;width:85px"></span>
</section>

<!-- footer -->
<footer class="footer">
  <h4 style="left:112px">MISSION STATEMENT</h4>
  <p class="mission">To multiply the gospel in urban centers by raising up and equipping church planters in a central city or multi-ethnic context."</p>
  <div class="f-brand"><span class="brand-dot"></span><span class="brand-name">Harborline Faith Builders</span></div>

  <h4 style="left:532px">QUICK LINKS</h4>
  <ul style="left:532px;top:100px"><li>Home</li><li>About Us</li><li>Donate</li><li>Contact Us</li><li>Partner</li></ul>

  <h4 style="left:710px">CONTACT US</h4>
  <div class="contact-row" style="top:106px"><svg class="pin" viewBox="0 0 9 12"><path d="M4.5 0A4.5 4.5 0 0 0 0 4.5C0 8 4.5 12 4.5 12S9 8 9 4.5A4.5 4.5 0 0 0 4.5 0z" fill="#f26b1d"/></svg><span>14 Harbor Row,<br>Riverton 25ZP</span></div>
  <div class="contact-row" style="top:164px"><svg class="pin" viewBox="0 0 9 12"><path d="M2 0l2 3-1 1.2c.5 1.4 1.5 2.5 2.8 3.1L7 6l2 2-1 2.5C4 10 .5 5 0 1z" fill="#f26b1d"/></svg><span>+1 (555) 014 2290</span></div>
  <div class="contact-row" style="top:212px"><svg class="pin" style="width:12px;height:9px" viewBox="0 0 12 9"><rect width="12" height="9" fill="#f26b1d"/><path d="M0 0l6 5 6-5" stroke="#2a2a2a" fill="none"/></svg><span>info@harborlinefaith.org</span></div>

  <h4 style="left:992px">FOLLOW US</h4>
  <div class="social" style="top:100px"><i></i>Community</div>
  <div class="social" style="top:135px"><i></i>Updates</div>
  <div class="social" style="top:170px"><i></i>Network</div>
  <div class="social" style="top:205px"><i></i>Gallery</div>

  <p class="copy">COPYRIGHT &copy; 2021 <b>HARBORLINE FAITH BUILDERS</b>. ALL RIGHTS RESERVED.</p>
</footer>

</body>
</html>
```